Letterhead Design Project

Looking for letterhead designs for Brastova Mining.

I am looking for a letterhead design in conjunction with a business card design. I have opened contests for both but ask that if you submit a letterhead design you also submit a business card design with a corresponding look/feel.

Brastova Mining is a B2B company that buys and sells large machinery tires within the coal mining industry. The design should the strong, crisp and masculine. I have uploaded the company logo and mock-up of the back of the company's business card.

Color scheme should be grey/green/black

Contact information to include:
Name: Dale Whitford
Title: Managing Director
Phone: 555-231-4097
Address: 1817 Pellam #3 Dallas, TX 75290
Email: Dale@Brastova.example
Updates

Project Deadline Extended
Reason: Looking for a more refined, elegant letterhead than what's been submitted as of yet. Here is a sample of what we're looking for: http://www.plumcrestgallery.example/letterhead-designs/ We will also be increasing the payment.

Industry/Entity Type

Coal Mining

```html
<!DOCTYPE html>
<html lang="en">
<head>
<meta charset="utf-8">
<title>Brastova Mining Letterhead</title>
<link rel="stylesheet" href="https://fonts.googleapis.com/css2?family=Montserrat:wght@400;600;700&display=swap">
<style>
  :root {
    --backdrop: #a9abb4;
    --paper: #f3f4f7;
    --ink-dark: #3a3d44;
    --ink-mid: #6b6f78;
    --accent-green: #5cb82e;
    --rule: #c9ccd3;
  }
  * { box-sizing: border-box; margin: 0; padding: 0; }
  html, body {
    width: 1200px;
    height: 1000px;
    overflow: hidden;
    background: var(--backdrop);
    font-family: "Montserrat", Arial, sans-serif;
  }
  .canvas {
    width: 1200px;
    height: 1000px;
    display: flex;
    align-items: center;
    justify-content: center;
  }
  .letterhead {
    position: relative;
    width: 712px;
    height: 920px;
    background: var(--paper);
    box-shadow: 0 6px 24px rgba(40, 42, 50, 0.18);
  }
  .letterhead-header {
    position: absolute;
    top: 64px;
    left: 60px;
    right: 60px;
    display: flex;
    align-items: flex-start;
    gap: 28px;
  }
  .sender-name {
    font-size: 11px;
    font-weight: 700;
    letter-spacing: 0.08em;
    text-transform: uppercase;
    color: var(--ink-dark);
  }
  .sender-title {
    margin-top: 3px;
    font-size: 10px;
    font-weight: 400;
    color: var(--accent-green);
  }
  .contact-block {
    padding-left: 14px;
    border-left: 1px solid var(--rule);
    margin-top: 28px;
    font-size: 9.5px;
    line-height: 1.55;
    color: var(--ink-mid);
  }
  .contact-label {
    color: var(--accent-green);
    font-weight: 600;
    margin-right: 3px;
  }
  .address-block { margin-top: 60px; }
  .brand-mark {
    position: absolute;
    top: 170px;
    right: 60px;
    display: flex;
    align-items: center;
    gap: 10px;
  }
  .brand-square {
    width: 22px;
    height: 22px;
    background: var(--accent-green);
  }
  .brand-name {
    font-size: 24px;
    font-weight: 600;
    letter-spacing: 0.06em;
    text-transform: uppercase;
    color: var(--ink-dark);
  }
</style>
</head>
<body>
  <main class="canvas">
    <article class="letterhead">
      <header class="letterhead-header">
        <div class="sender">
          <p class="sender-name">Dale Whitford</p>
          <p class="sender-title">Managing Director</p>
        </div>
        <div class="contact-block phone-email-block">
          <p><span class="contact-label">P:</span>555-231-4097</p>
          <p><span class="contact-label">E:</span>Dale@Brastova.example</p>
        </div>
        <div class="contact-block address-block">
          <p>1817 Pellam #3</p>
          <p>Dallas, TX 75290</p>
        </div>
      </header>
      <div class="brand-mark">
        <span class="brand-square" aria-hidden="true"></span>
        <span class="brand-name">Brastova Mining</span>
      </div>
    </article>
  </main>
</body>
</html>
```